Quick Order Banner Design

We want to build a banner that will sit in the middle of the page that will replace our current quick order banner that we don't like. See https://www.snapglimmer.com/image/48273916?key=3f9b2c81d4e6a07f5c1b9e2d7a84f630

Text:
Quick Order is a fast and easy way to fill your cart with items when you know exactly what you want to purchase.

Design ideas:

Use foto Noto Sans. Color codes can be of #00539E, FDBC38, #6AC07A

We don't want a computer screen in banner nor a person. You can look at our competitors below for ideas.

i don't like the design here https://toblinmobilebits.com/blog/post/order-parts-fast-with-our-new-quick-order-feature but the concept is cool as it shows where to access it.. but i want other ideas too.

Our staging server is pelvant7.com

Our competitors:
https://www.quillonsupply.com/
https://www.brevolt.com/
https://www.zoska.com/
https://www.vimbo.com/index.html

Target Market(s)

B2B, Contractors who buy our products

Industry/Entity Type

hvac

Requirements
Should not have
• people photos or computer or computer screens.

```html
<!DOCTYPE html>
<html lang="en">
<head>
<meta charset="utf-8">
<title>Quick Order Banner</title>
<link rel="stylesheet" href="https://fonts.googleapis.com/css2?family=Noto+Sans:ital,wdth,wght@0,62.5..100,400;0,62.5..100,700;0,62.5..100,800;1,62.5..100,900&display=swap">
<style>
  :root {
    --page-bg: #ffffff;
    --brand-blue: #00539e;
    --brand-blue-deep: #003f7d;
    --brand-blue-light: #0a63b3;
    --accent-green: #6ac07a;
    --accent-green-soft: rgba(106, 192, 122, 0.55);
    --accent-green-faint: rgba(106, 192, 122, 0.22);
    --accent-orange: #f28a2e;
    --shadow-navy: #0b2a55;
    --text-white: #ffffff;
  }
  * { margin: 0; padding: 0; box-sizing: border-box; }
  html, body {
    width: 1200px;
    height: 817px;
    overflow: hidden;
    background: var(--page-bg);
    font-family: "Noto Sans", Arial, sans-serif;
  }
  .banner {
    position: absolute;
    left: 140px;
    top: 263px;
    width: 933px;
    height: 298px;
    overflow: hidden;
    background: radial-gradient(ellipse at 55% 50%, var(--brand-blue-light) 0%, var(--brand-blue) 45%, var(--brand-blue-deep) 100%);
  }
  .title-frame-area {
    position: absolute;
    left: 57px;
    top: 50px;
    width: 99px;
    height: 160px;
    border-radius: 6px;
    background: linear-gradient(160deg, var(--accent-green-soft), var(--accent-green-faint));
  }
  .banner-title {
    position: absolute;
    left: 97px;
    top: 76px;
    font-size: 71px;
    line-height: 1;
    font-weight: 900;
    font-style: italic;
    font-stretch: 84%;
    letter-spacing: -1px;
    color: var(--text-white);
    text-shadow: 3px 4px 0 var(--shadow-navy);
    white-space: nowrap;
  }
  .banner-copy {
    position: absolute;
    left: 167px;
    top: 158px;
    width: 440px;
    font-size: 24.5px;
    line-height: 27.5px;
    font-weight: 400;
    color: var(--text-white);
  }
  .banner-copy strong { font-weight: 800; }
  .cart-art-area {
    position: absolute;
    left: 613px;
    top: 30px;
    width: 227px;
    height: 178px;
    border-radius: 10px;
    background: linear-gradient(135deg, var(--accent-green-soft), var(--accent-green-faint));
  }
  .cta-button {
    position: absolute;
    left: 613px;
    top: 213px;
    width: 271px;
    height: 56px;
    border-radius: 28px;
    background: var(--accent-orange);
    box-shadow: 4px 5px 0 var(--shadow-navy);
    color: var(--text-white);
    font-size: 29px;
    font-weight: 800;
    display: flex;
    align-items: center;
    justify-content: center;
    gap: 8px;
    text-decoration: none;
    letter-spacing: 0.3px;
  }
  .cta-button svg { width: 26px; height: 22px; }
</style>
</head>
<body>
  <section class="banner">
    <div class="title-frame-area" role="img" aria-label="Green angled frame accent behind the title"></div>

    <h1 class="banner-title">QUICK ORDER</h1>

    <p class="banner-copy"><strong>FAST AND EASY WAY</strong> to fill your cart with items when you know exactly what you want to purchase.</p>

    <div class="cart-art-area" role="img" aria-label="Green shopping cart illustration with speed lines"></div>

    <a class="cta-button" href="#">TRY NOW
      <svg viewBox="0 0 26 22" aria-hidden="true">
        <path d="M3 3 L11 11 L3 19 M14 3 L22 11 L14 19" fill="none" stroke="var(--text-white)" stroke-width="4.5" stroke-linecap="round" stroke-linejoin="round"/>
      </svg>
    </a>
  </section>
</body>
</html>
```